Real Estate Sales Brokerage

Design a modern and fresh looking standard size business card, incorporate our logo's color scheme and modern appearance with head shot photo on front side and incorporate our log on the back side

Target Market(s)

Residential Home sales

Industry/Entity Type

Real Estate Agent

Font styles to use
Sans Serif

Colors

Designer to choose colors to be used in the design.

Requirements
Must have
• fresh, modern, not too busy, incorporate head shot in front of the card, incorporate logo in front and back of the card. Use logo design scheme as appropriate.
Nice to have
• horizontal and vertical options to compare would be nice.

```html
<!DOCTYPE html>
<html lang="en">
<head>
<meta charset="utf-8">
<title>Harborview Home Realty – Business Card</title>
<link href="https://fonts.googleapis.com/css2?family=Roboto:wght@400;500;700&display=swap" rel="stylesheet">
<style>
  :root {
    --olive: #6f6a2b;
    --gold: #f0d23c;
    --ink: #4a4a4a;
    --paper: #ffffff;
    --backdrop: #2f2f2f;
    --suit: #2f4f86;
    --suit-light: #5a7bb3;
  }
  * { box-sizing: border-box; margin: 0; padding: 0; }
  html, body { width: 1200px; height: 801px; overflow: hidden; }
  body {
    background: var(--backdrop);
    font-family: "Roboto", Arial, sans-serif;
    display: flex;
    align-items: center;
    justify-content: center;
    gap: 48px;
  }
  .card {
    width: 525px;
    height: 300px;
    background: var(--paper);
    position: relative;
    overflow: hidden;
    box-shadow: 0 8px 24px rgba(0,0,0,.35);
  }
  /* Front */
  .front .brand-small {
    position: absolute; left: 34px; top: 30px;
    display: flex; align-items: center; gap: 8px;
    color: var(--olive); font-weight: 500; font-size: 13px;
    letter-spacing: .06em; text-transform: uppercase;
  }
  .brand-mark { width: 12px; height: 12px; background: var(--olive); }
  .front .details { position: absolute; left: 34px; top: 86px; }
  .agent-name {
    color: var(--gold); font-weight: 700; font-size: 22px;
    letter-spacing: .02em; text-transform: uppercase;
  }
  .agent-role {
    color: var(--ink); font-size: 11px; letter-spacing: .12em;
    text-transform: uppercase; margin-top: 4px;
  }
  .contact-list { list-style: none; margin-top: 16px; }
  .contact-list li {
    display: flex; align-items: center; gap: 10px;
    color: var(--ink); font-size: 12.5px; letter-spacing: .05em;
    line-height: 20px;
  }
  .contact-list svg { width: 12px; height: 12px; flex: none; }
  .address { color: var(--ink); font-size: 12.5px; letter-spacing: .05em; line-height: 18px; margin-top: 12px; }
  .web { color: var(--ink); font-weight: 500; font-size: 12.5px; letter-spacing: .06em; margin-top: 10px; }
  .headshot {
    position: absolute; right: 0; top: 0; width: 230px; height: 100%;
    background: linear-gradient(180deg, #f4f4f4 0%, #e9e6e2 28%, var(--suit-light) 52%, var(--suit) 100%);
  }
  /* Back */
  .back {
    display: flex; flex-direction: column; align-items: center; justify-content: center;
  }
  .brand-large {
    display: flex; align-items: center; gap: 18px;
    color: var(--olive); font-weight: 500; font-size: 30px;
    letter-spacing: .06em; text-transform: uppercase; line-height: 1.1;
  }
  .brand-large .brand-mark { width: 34px; height: 34px; }
  .back .web { margin-top: 40px; }
</style>
</head>
<body>
  <section class="card front">
    <div class="brand-small"><span class="brand-mark"></span>Harborview Home Realty</div>
    <div class="details">
      <p class="agent-name">Dan Weller</p>
      <p class="agent-role">Director</p>
      <ul class="contact-list">
        <li><svg viewBox="0 0 12 12"><rect x="1.5" y="1.5" width="9" height="9" rx="1.5" fill="none" stroke="#f0d23c" stroke-width="1.5"/></svg>555 010 2040</li>
        <li><svg viewBox="0 0 12 12"><path d="M2 1.5h2.5l1 2.5-1.5 1a6 6 0 0 0 3 3l1-1.5 2.5 1V10a1 1 0 0 1-1 1A9 9 0 0 1 1 2.5a1 1 0 0 1 1-1z" fill="#f0d23c"/></svg>555 010 2041</li>
        <li><svg viewBox="0 0 12 12"><rect x="3" y="1" width="6" height="4" fill="#f0d23c"/><rect x="1" y="5" width="10" height="6" rx="1" fill="#f0d23c"/></svg>+1 555 010 2099</li>
        <li><svg viewBox="0 0 12 12"><rect x="1" y="2.5" width="10" height="7" fill="none" stroke="#f0d23c" stroke-width="1.3"/><path d="M1 2.5l5 4 5-4" fill="none" stroke="#f0d23c" stroke-width="1.3"/></svg>dan@harborviewre.com</li>
      </ul>
      <p class="address">418 Maple Row, Brookfield<br>CA 90000, United States</p>
      <p class="web">www.harborviewre.com</p>
    </div>
    <div class="headshot" role="img" aria-label="Headshot of the agent in a blue suit and red tie"></div>
  </section>

  <section class="card back">
    <div class="brand-large"><span class="brand-mark"></span><span>Harborview<br>Home<br>Realty</span></div>
    <p class="web">www.harborviewre.com</p>
  </section>
</body>
</html>
```